Project Management - Web Design Project

Vantrel 4 Management Limited is a company which provides specialist Project Control and Contract Management expertise to the Engineering, Construction and Manufacturing industries. The emphasis is on advanced Project Management techniques in particular Planning & Scheduling, Cost Control, Change Control, Risk Management, Reporting and Contract Administration. We are a global company (albeit a small start-up at this time) and pride ourselves on our ability to support projects to help them achieve their goals and objectives. Our aim is to implement work class control tools in a simple and user friendly manner. We would like the website to appear professional but at the same time easy to navigate and a good balance between text and pictures. The final design should communicate our value added service to our customers, our willingness to support and our structured approach to our work.

Target Market(s)

Project Management professionals working for engineering, construction and manufacturing organisations involved with delivering projects.

Industry/Entity Type

Construction

Requirements
Must have
• The website must include all of the content from the attached Excel brief. The company logo (attached) must also be included in the design. The design must portray a professional look and feel. Please include pictures and photographs related to project management in the engineering, construction and manufacturing industries. We may supplement with pictures of our own during the next steps.
Nice to have
• Emphasis that Vantrel 4 is available to support, guide, direct to achieve positive outcomes for the projects. We work hard at developing our customer relationships. Our employees are experienced in advanced project management techniques.
Should not have
• The design should not use old style fonts. It should look modern and professional. Do not include cartoons or silly illustrations.

```html
<!DOCTYPE html>
<html lang="en">
<head>
<meta charset="utf-8">
<title>Vantrel 4 Management Limited</title>
<link href="https://fonts.googleapis.com/css2?family=Arimo:wght@400;700&family=Source+Sans+3:wght@400;600&display=swap" rel="stylesheet">
<style>
:root{
  --bg:#dcdcdc;
  --page:#ffffff;
  --dark:#2b2b2b;
  --darker:#1e1e1e;
  --blue:#1a6fc9;
  --text:#333333;
  --muted:#555555;
  --panel:#ececec;
  --line:#d5d5d5;
  --brand:#4a4f57;
}
*{margin:0;padding:0;box-sizing:border-box}
html,body{width:1093px;height:1200px;overflow:hidden}
body{background:linear-gradient(135deg,#e8e8e8,#d2d2d2 50%,#e4e4e4);font-family:"Arimo",Arial,sans-serif;color:var(--text);position:relative}
.page{position:absolute;left:152px;top:54px;width:790px;height:1090px;background:var(--page);box-shadow:0 0 6px rgba(0,0,0,.25)}
.abs{position:absolute}
.brand{left:23px;top:80px;width:112px;text-align:center;color:var(--brand)}
.brand-name{font-family:"Source Sans 3",sans-serif;font-size:19px;font-weight:600;letter-spacing:1px;line-height:20px;white-space:nowrap}
.brand-sub{font-family:"Source Sans 3",sans-serif;font-size:7px;font-weight:600;letter-spacing:1px;white-space:nowrap}
.utility{right:27px;top:44px;font-size:8px;color:#333;word-spacing:2px;white-space:nowrap}
.search{left:613px;top:67px;width:149px;height:18px;border:1px solid var(--line);font-size:8px;color:#999;padding:4px 6px}
.search svg{position:absolute;right:3px;top:2px}
.search i{position:absolute;right:20px;top:2px;width:1px;height:12px;background:var(--line)}
.nav{left:158px;top:91px;width:607px;height:24px;background:linear-gradient(#3a3a3a,var(--darker));border-radius:3px;display:flex;justify-content:space-between;align-items:center;padding:0 6px 0 9px;font-size:11px;color:#fff;white-space:nowrap}
.dropdown{left:333px;top:115px;width:129px;height:134px;background:linear-gradient(#2e2e2e,#1c1c1c);border-radius:0 0 3px 3px;font-size:9.5px;color:#fff;padding-top:10px}
.dropdown li{list-style:none;height:20px;padding-left:7px;line-height:16px}
.dropdown li.active{background:#404040;margin-top:-4px;padding-top:4px;height:20px}
.hero{left:23px;top:140px;width:741px;height:325px;border:1px solid #e4e4e4;
  background:linear-gradient(90deg,#d9d9db 0%,#8a8d93 14%,#3a3c42 22%,#c9cacd 34%,#efefef 50%,#e3e3e5 62%,#9aa1ac 76%,#e8e8e8 86%,#5a5c62 94%,#efefef 100%)}
.slider{left:23px;top:472px;width:741px;height:34px;background:#e6e6e6}
.about-panel{left:23px;top:523px;width:739px;height:121px;background:linear-gradient(#f4f4f4,#e6e6e6)}
.section-title{font-family:"Source Sans 3",sans-serif;font-weight:400;font-size:15px;color:var(--blue);white-space:nowrap}
.about-title{left:30px;top:536px}
.about-text{left:30px;top:565px;width:379px;font-size:10px;line-height:12px;text-align:justify;color:#333}
.read-link{left:30px;top:630px;font-size:10.5px;color:var(--blue)}
.divider{left:424px;top:536px;height:100px;border-left:1px dotted #bbb}
.projects-title{left:444px;top:536px}
.badge{top:564px;width:67px;height:66px;background:#fff;border:1px solid #ccc;border-radius:6px;box-shadow:0 1px 3px rgba(0,0,0,.25);display:flex;align-items:center;justify-content:center}
.badge span{width:44px;height:44px;background:#8a8a8a;border-radius:4px}
.card{top:656px;width:181px;height:228px;background:var(--panel);border-radius:4px}
.card-head{height:27px;background:linear-gradient(#3a3a3a,var(--darker));border-radius:4px 4px 0 0;font-family:"Source Sans 3",sans-serif;font-size:13.5px;color:#fff;padding:5px 9px;white-space:nowrap}
.card-photo{margin:9px 7px 0;height:90px}
.card-text{padding:9px 8px 0;font-size:8.5px;line-height:11.4px;color:#333;height:73px}
.btn{margin-left:9px;display:inline-block;background:var(--dark);color:#fff;font-size:9px;padding:4px 3px;border-radius:2px}
.rule{left:0;top:902px;width:790px;border-top:1px solid #e2e2e2}
.footer-col{top:914px;font-size:9px;color:#444;white-space:nowrap}
.footer-col h3{font-family:"Source Sans 3",sans-serif;font-weight:400;font-size:13px;color:#222;margin-bottom:12px}
.footer-col li{list-style:none;height:20px}
.legal{left:240px;top:1042px;width:300px;text-align:center;font-size:7.5px;color:#444;line-height:13px;word-spacing:2px;white-space:nowrap}
.legal b{font-weight:400;font-size:9px}
.social{left:618px;top:1041px;display:flex;gap:3px}
.social span{width:26px;height:26px;border-radius:50%;background:#3d6fb0;border:2px solid #e6e6e6;box-shadow:0 1px 2px rgba(0,0,0,.3)}
</style>
</head>
<body>
<div class="page">
  <div class="abs brand">
    <div class="brand-name">VANTREL 4</div>
    <div class="brand-sub">MANAGEMENT LIMITED</div>
  </div>
  <div class="abs utility">My Account &nbsp;I&nbsp; Login &nbsp;I&nbsp; Technica Support &nbsp;I&nbsp; Contact</div>
  <div class="abs search">Search<i></i>
    <svg width="13" height="13" viewBox="0 0 13 13"><circle cx="5.5" cy="5.5" r="4" fill="none" stroke="#777" stroke-width="1.2"/><line x1="8.5" y1="8.5" x2="12" y2="12" stroke="#777" stroke-width="1.4"/></svg>
  </div>
  <nav class="abs nav">
    <span>Home</span><span>Introduction</span><span>Project Control</span><span>Contract Managemen</span><span>Specialist Services</span><span>Projects</span>
  </nav>
  <div class="abs hero" role="img" aria-label="Business people in dark suits assembling large white puzzle pieces"></div>
  <ul class="abs dropdown">
    <li class="active">General</li><li>Cost Control</li><li>Change Control</li><li>Claim Analysis</li><li>General</li><li>Cost Control</li>
  </ul>
  <div class="abs slider">
    <svg width="741" height="34" viewBox="0 0 741 34">
      <polyline points="28,6 14,17 28,28" fill="none" stroke="#bbb" stroke-width="3"/>
      <polyline points="713,6 727,17 713,28" fill="none" stroke="#bbb" stroke-width="3"/>
      <line x1="18" y1="17" x2="723" y2="17" stroke="#c4c4c4" stroke-width="2"/>
      <rect x="594" y="10" width="58" height="14" rx="7" fill="#bdbdbd"/>
    </svg>
  </div>
  <div class="abs about-panel"></div>
  <h2 class="abs section-title about-title">ABOUT VANTREL 4 MANAGEMENT &nbsp;LIMITED</h2>
  <p class="abs about-text">Vantrel 4 Management Limited provide project control and contract management expertiese to the Engineering / Construction and Manufacturing industries. We are able to draw from the vast experience of our specialist resource base . Our employees have considerable experience gained from direct involvement on numerous large scale international projects.</p>
  <span class="abs read-link">READ MORE..</span>
  <div class="abs divider"></div>
  <h2 class="abs section-title projects-title">PROJECTS</h2>
  <div class="abs badge" style="left:447px"><span></span></div>
  <div class="abs badge" style="left:527px"><span style="border-radius:50%"></span></div>
  <div class="abs badge" style="left:607px"><span></span></div>
  <div class="abs badge" style="left:688px"><span style="background:#d0d0d0"></span></div>

  <section class="abs card" style="left:25px">
    <div class="card-head">INTRODUCTION</div>
    <div class="card-photo" role="img" aria-label="Team gathered around a laptop" style="background:linear-gradient(135deg,#e9e9ea,#7d7a78 55%,#dcdcdc)"></div>
    <p class="card-text">Our Project Control System (PCS) is based on the establishment of an approved project baseline.<br>The baseline is developed within a reasonable</p>
    <span class="btn">READ MORE</span>
  </section>
  <section class="abs card" style="left:211px">
    <div class="card-head">PROJECT CONTROL</div>
    <div class="card-photo" role="img" aria-label="Presenter at a flip chart with colleagues" style="background:linear-gradient(90deg,#d8d8da,#45474d 45%,#f3f3f3 70%,#5c5e64)"></div>
    <p class="card-text">Project Control is an independent function reporting directly to the Project Director and is often described as the conscience of a project. Nowadays most projects are managed in a matrix organisation.</p>
    <span class="btn">READ MORE</span>
  </section>
  <section class="abs card" style="left:397px">
    <div class="card-head">CONTRACT MANAGEMENT</div>
    <div class="card-photo" role="img" aria-label="Hands reviewing construction plans with pencils" style="background:linear-gradient(135deg,#d9b89e,#ecebea 50%,#c7a58c)"></div>
    <p class="card-text">Effective Contract Management is essential for a project to be successful. The contract represents the agreed rights and obligations made by each party to one another.</p>
    <span class="btn">READ MORE</span>
  </section>
  <section class="abs card" style="left:582px">
    <div class="card-head">SPECIALIST SERVICES</div>
    <div class="card-photo" role="img" aria-label="Hand with pen over printed charts" style="background:linear-gradient(135deg,#5a87c0,#dfe7f0 50%,#9db6d6)"></div>
    <p class="card-text">The greatest opportunity to positively or negatively affect the outcome of a project, both in terms of schedule and budget, is during the Engineering phase</p>
    <span class="btn">READ MORE</span>
  </section>

  <div class="abs rule"></div>
  <div class="abs footer-col" style="left:46px"><h3>ABOUT VANTREL 4</h3><ul><li>Office Locations</li><li>Career Opportunities</li><li>Contact Norlio</li><li>Executive Profiles</li></ul></div>
  <div class="abs footer-col" style="left:231px"><h3>PROJECT CONTROL</h3><ul><li>General</li><li>Cost Control</li><li>Change Control</li><li>Claim Analysis</li></ul></div>
  <div class="abs footer-col" style="left:419px"><h3>SPECIALIST SERVICES</h3><ul><li>Engineering Earned Value</li><li>S-Curve Reporting</li><li>Critical Issues Reporting</li><li>Management Schedules</li></ul></div>
  <div class="abs footer-col" style="left:599px"><h3>CONTRACT MANAGEMENT</h3><ul><li>Start Selling with Norlio Today!</li><li>Request Additional Information</li></ul></div>

  <div class="abs legal">Home &nbsp; | &nbsp; Contact us &nbsp; | &nbsp; Privacy statement &nbsp; | &nbsp; Terms of use<br>© 2012 <b>Vantrel 4</b> TM &nbsp; All Rights Reserved</div>
  <div class="abs social" aria-label="Social links"><span></span><span></span><span style="background:#c44"></span><span style="background:#3b9bd6"></span></div>
</div>
</body>
</html>
```